Book design for Martial Arts Business

TITLE : The Lantern Ledger Method

Subtitle : " Master your business , Master your life

Author Hollis Penwarden

I need a book cover design for my new book which is on Martial Arts Busines Success.

Simple and Powerful Black and red in Design
Strong font , thats clear and easy to read
the Tag line of the book is " Master your business, Master your life ( I want this to stand out )

Front cover image with dojo

Back image of myself

space for 2 endorsement and writing about the book

I dont want it to look cheesy or American must have an uk feel too

No money on the book whatsoever

I have attached a design so far for you to see but want variations
Updates

Reason: Not quite got the look on this we will have to extend this

Need extra days to review

Need extra days to review

Target Market(s)

Martial Arts Business owners

Industry/Entity Type

Business

Colors
000000
ec1f27

Requirements
Must have
• Red and Black in colour
• good font thats not standard .. Impactful and clear
• Images used and any other ideas
Nice to have
• No money in it
Should not have
• Clear and powerful design

```html
<!DOCTYPE html>
<html lang="en">
<head>
<meta charset="utf-8">
<title>The Lantern Ledger Method – Book Cover</title>
<link rel="stylesheet" href="https://fonts.googleapis.com/css2?family=Bebas+Neue&family=Montserrat:ital,wght@0,400;0,500;0,600;1,400&display=swap">
<style>
  :root {
    --ink: #000000;
    --charcoal: #231f20;
    --brand-red: #ec1f27;
    --deep-red: rgba(110, 8, 14, 0.82);
    --white: #ffffff;
    --title-font: "Bebas Neue", "Oswald", sans-serif;
    --text-font: "Montserrat", Arial, sans-serif;
  }
  * { box-sizing: border-box; margin: 0; padding: 0; }
  html, body {
    width: 1200px; height: 778px; overflow: hidden;
    background: var(--charcoal);
  }
  .cover-wrap {
    position: relative; width: 1200px; height: 778px; overflow: hidden;
    font-family: var(--text-font); color: var(--white);
  }

  /* ---------- Back cover ---------- */
  .back-cover {
    position: absolute; left: 0; top: 0; width: 616px; height: 778px;
    background: var(--charcoal);
  }
  .author-band { position: absolute; left: 0; top: 0; width: 616px; height: 182px; }
  .author-band__name {
    position: absolute; left: 58px; top: 52px;
    font-weight: 600; font-size: 22px; letter-spacing: 0.3px; line-height: 1;
  }
  .author-band__bio {
    position: absolute; left: 58px; top: 78px; width: 320px;
    font-size: 10.4px; line-height: 13px;
  }
  .author-portrait {
    position: absolute; left: 412px; top: 46px; width: 128px; height: 136px;
    background: linear-gradient(180deg, #3a3435 0%, #191616 55%, #4a1014 100%);
  }

  .synopsis-band {
    position: absolute; left: 0; top: 182px; width: 616px; height: 296px;
    background: var(--brand-red);
  }
  .synopsis-band__title {
    position: absolute; left: 52px; top: 18px;
    font-family: var(--title-font); font-size: 55px; line-height: 1;
    letter-spacing: 0.2px; color: var(--white);
    text-shadow: 2px 2px 3px rgba(0,0,0,0.35);
  }
  .synopsis-band__text {
    position: absolute; left: 56px; top: 77px; width: 515px;
    font-size: 12.6px; line-height: 15.2px;
  }

  .endorsements { position: absolute; left: 56px; top: 503px; width: 502px; }
  .endorsement { margin-bottom: 13px; }
  .endorsement__quote { font-style: italic; font-size: 12.4px; line-height: 15.2px; }
  .endorsement__name {
    text-align: right; font-weight: 500; font-size: 12.4px; line-height: 15px; margin-top: 3px;
  }
  .isbn-panel {
    position: absolute; left: 392px; top: 637px; width: 166px; height: 81px;
    background: var(--white);
  }

  /* ---------- Spine ---------- */
  .spine { position: absolute; left: 584px; top: 0; width: 32px; height: 778px; }
  .spine__author, .spine__title {
    position: absolute; left: 50%; white-space: nowrap;
    transform-origin: 0 0; transform: rotate(90deg);
  }
  .spine__author {
    top: 48px; margin-left: 7px;
    font-weight: 500; font-size: 11px; letter-spacing: 0.6px; color: var(--white);
  }
  .spine__title {
    top: 196px; margin-left: 13px;
    font-family: var(--title-font); font-size: 27px; letter-spacing: 0.3px; color: var(--charcoal);
  }

  /* ---------- Front cover ---------- */
  .front-cover { position: absolute; left: 616px; top: 0; width: 584px; height: 778px; }
  .dojo-photo {
    position: absolute; inset: 0;
    background:
      linear-gradient(180deg, #d9252e 0%, #c41a24 35%, #8e1419 48%, #3a3a3a 52%, #2d3230 66%, #d6414b 78%, #a41a22 100%);
  }
  .instructor-photo {
    position: absolute; left: 44px; top: 396px; width: 190px; height: 382px;
    background: linear-gradient(180deg, #c8a08c 0%, #1c1a1b 22%, #121112 100%);
    border-radius: 60px 60px 0 0;
  }
  .front-cover__author {
    position: absolute; right: 68px; top: 50px;
    font-weight: 600; font-size: 29px; letter-spacing: 0.3px; line-height: 1;
  }
  .front-cover__title {
    position: absolute; left: 44px; top: 92px;
    font-family: var(--title-font); font-size: 98px; line-height: 94px;
    letter-spacing: 0.5px; color: var(--white);
    text-shadow: 4px 4px 6px rgba(0,0,0,0.45);
  }
  .tagline-band {
    position: absolute; left: 136px; top: 560px; width: 448px; height: 110px;
    background: var(--deep-red);
    display: flex; flex-direction: column; justify-content: center; align-items: center;
  }
  .tagline-band__line {
    font-weight: 600; font-size: 26.5px; line-height: 35px; letter-spacing: 0.3px;
    text-transform: uppercase;
  }
</style>
</head>
<body>
<div class="cover-wrap">

  <section class="back-cover">
    <div class="author-band">
      <h2 class="author-band__name">HOLLIS PENWARDEN</h2>
      <p class="author-band__bio">Lorem ipsum dolor sit amet, consectetur adipisicing elit, sed do eiusmod tempor incididunt ut labore et dolore magna aliqua. Ut enim ad minim veniam, quis nostrud exercitation ullamco laboris nisi ut aliquip ex ea commodo consequat. Duis aute irure dolor in reprehenderit in voluptate velit esse cillum dolore eu fugiat nulla pariatur.</p>
      <div class="author-portrait" role="img" aria-label="Portrait photo of the author in a black and red training top"></div>
    </div>

    <div class="synopsis-band">
      <h2 class="synopsis-band__title">THE LANTERN LEDGER METHOD</h2>
      <p class="synopsis-band__text">Lorem ipsum dolor sit amet, consectetur adipisicing elit, sed do eiusmod tempor incididunt ut labore et dolore magna aliqua. Ut enim ad minim veniam, quis nostrud exercitation ullamco laboris nisi ut aliquip ex ea commodo consequat. Duis aute irure dolor in reprehenderit in voluptate velit esse cillum dolore eu fugiat nulla pariatur. Excepteur sint occaecat cupidatat non proident, sunt in culpa qui officia deserunt mollit anim id est laborum. Sed ut perspiciatis unde omnis iste natus error sit voluptatem accusantium doloremque laudantium, totam rem aperiam, eaque ipsa quae ab illo inventore veritatis et quasi architecto beatae vitae dicta sunt explicabo. Nemo enim ipsam voluptatem quia voluptas sit aspernatur aut odit aut fugit, sed quia consequuntur magni dolores eos qui ratione voluptatem sequi nesciunt. Neque porro quisquam est, qui dolorem ipsum quia dolor sit amet, consectetur, adipisci velit, sed quia non numquam eius modi tempora incidunt ut labore et dolore magnam aliquam quaerat voluptatem.</p>
    </div>

    <div class="endorsements">
      <blockquote class="endorsement">
        <p class="endorsement__quote">Lorem ipsum dolor sit amet, consectetur adipisicing elit, sed do eiusmod tempor incididunt ut labore et dolore magna aliqua.</p>
        <p class="endorsement__name">Jone Doe</p>
      </blockquote>
      <blockquote class="endorsement">
        <p class="endorsement__quote">Lorem ipsum dolor sit amet, consectetur adipisicing elit, sed do eiusmod tempor incididunt ut labore et dolore magna aliqua.</p>
        <p class="endorsement__name">Jane Doe</p>
      </blockquote>
    </div>

    <div class="isbn-panel"></div>
  </section>

  <section class="spine">
    <span class="spine__author">HOLLIS PENWARDEN</span>
    <span class="spine__title">THE LANTERN LEDGER METHOD</span>
  </section>

  <section class="front-cover">
    <div class="dojo-photo" role="img" aria-label="Red-lit martial arts dojo with dark training mats and hanging punch bags"></div>
    <div class="instructor-photo" role="img" aria-label="The author standing in the dojo wearing a black training top and black belt"></div>
    <p class="front-cover__author">HOLLIS PENWARDEN</p>
    <h1 class="front-cover__title">THE<br>LANTERN<br>LEDGER METHOD</h1>
    <div class="tagline-band">
      <span class="tagline-band__line">Master your business</span>
      <span class="tagline-band__line">Master your life</span>
    </div>
  </section>

</div>
</body>
</html>
```